Harlow Ironworks Business Card

We need a business card design for a new small metal fabrication business in rural NSW, Australia.

The business (Harlow Ironworks) is owner operated by a man with the initials KB - much of the branding comes from this name.

Harlow Ironworks designs, engineers, repairs and manufactures a range of custom, quality metal works including vehicle trays, agricultural machinery impliments, trailers, wood splitters, fire pits, furniture etc.

The brand position focuses on custom work of the highest quality.

Business card design should show quality, attention to detail and stand out among a mass of business cards.

Logos are in the files

The grey color may be changed on the logo if required to stand out more.

There is an image attached of a simple card that is liked because it is clean, clear, simple, masculine and effective. It says 'quality'. As most of the work we do is custom it would be good to have the business card speak to this.

Target Market(s)

Rural and regional based Australians. Primarily adult male 25-60 yrs. Primary production / rural / travelling lifestyle.

Industry/Entity Type

Metal Fabrication

Contact Information for Business Card

The words 'custom quality fabrications' would be great somewhere perhaps on the backside (not on the information side)
Name
title
Phone: 0418 539 746 and (02) 6193 4827
email: info@harlowiw.com.au
www.harlowiw.com.au

address (2 lines)

Requirements
Nice to have
• Background colour should be very navy blue or black.
Should not have
• NO orange and blue combinations.
• Navy is OK

```html
<!DOCTYPE html>
<html lang="en">
<head>
<meta charset="utf-8">
<title>Harlow Ironworks – Business Card</title>
<link href="https://fonts.googleapis.com/css2?family=Michroma&family=Arimo:wght@400&display=swap" rel="stylesheet">
<style>
  :root {
    --backdrop: #d9d9d7;
    --navy: #131a2b;
    --navy-shade: #1a2236;
    --paper: #f4f4f2;
    --steel: #8e8f91;
    --steel-light: #b4b5b6;
    --green: #57b13c;
    --ink: #6f7072;
    --white: #f2f2f2;
  }
  * { box-sizing: border-box; margin: 0; padding: 0; }
  html, body { width: 1200px; height: 900px; overflow: hidden; }
  body {
    background: var(--backdrop);
    display: flex;
    flex-direction: column;
    align-items: center;
    justify-content: center;
    gap: 24px;
  }
  .card {
    position: relative;
    width: 680px;
    height: 416px;
    overflow: hidden;
    box-shadow: 0 6px 18px rgba(0,0,0,0.18);
  }

  /* Back side */
  .card--back {
    background: var(--navy);
    color: var(--white);
  }
  .card--back .back-shape {
    position: absolute;
    right: -60px;
    top: -40px;
    width: 380px;
    height: 480px;
    background: var(--navy-shade);
    transform: skewX(-12deg);
  }
  .back-brand {
    position: absolute;
    left: 0; right: 0;
    top: 130px;
    display: flex;
    align-items: center;
    justify-content: center;
    gap: 18px;
  }
  .back-brand .brand-mark {
    width: 22px; height: 22px;
    background: var(--white);
  }
  .back-brand .brand-name {
    font-family: "Michroma", sans-serif;
    font-size: 36px;
    line-height: 1.15;
    letter-spacing: 3px;
    color: var(--white);
  }
  .tagline {
    position: absolute;
    left: 0; right: 0;
    top: 268px;
    text-align: center;
    font-family: "Michroma", sans-serif;
    font-size: 14px;
    letter-spacing: 5px;
    color: var(--white);
  }

  /* Front side */
  .card--front { background: var(--paper); }
  .front-brand {
    position: absolute;
    left: 40px;
    top: 110px;
    width: 270px;
    display: flex;
    flex-direction: column;
    align-items: center;
    gap: 18px;
  }
  .front-brand .brand-mark {
    width: 46px; height: 46px;
    background: var(--green);
  }
  .front-brand .brand-name {
    font-family: "Michroma", sans-serif;
    font-size: 26px;
    line-height: 1.2;
    letter-spacing: 2px;
    text-align: center;
    color: var(--steel);
  }
  .divider {
    position: absolute;
    left: 336px;
    top: 108px;
    width: 1.5px;
    height: 170px;
    background: var(--steel-light);
  }
  .contact {
    position: absolute;
    left: 366px;
    top: 112px;
  }
  .contact .person {
    font-family: "Michroma", sans-serif;
    font-size: 20px;
    letter-spacing: 1.5px;
    color: var(--green);
  }
  .contact .role {
    font-family: "Arimo", sans-serif;
    font-size: 16px;
    letter-spacing: 1px;
    color: var(--ink);
    margin: 2px 0 10px;
  }
  .contact ul { list-style: none; }
  .contact li {
    display: flex;
    align-items: center;
    gap: 8px;
    font-family: "Arimo", sans-serif;
    font-size: 17px;
    letter-spacing: 1px;
    color: var(--ink);
    line-height: 24px;
  }
  .contact li svg { width: 15px; height: 15px; flex: none; }
  .foot-bands {
    position: absolute;
    left: 0; bottom: 0;
    width: 680px; height: 60px;
  }
</style>
</head>
<body>

  <section class="card card--back" aria-label="Business card, back">
    <div class="back-shape"></div>
    <div class="back-brand">
      <span class="brand-mark"></span>
      <span class="brand-name">HARLOW<br>IRONWORKS</span>
    </div>
    <p class="tagline">THE WORDS 'CUSTOM QUALITY FABRICATIONS</p>
  </section>

  <section class="card card--front" aria-label="Business card, front">
    <div class="front-brand">
      <span class="brand-mark"></span>
      <span class="brand-name">HARLOW<br>IRONWORKS</span>
    </div>

    <div class="divider"></div>

    <div class="contact">
      <p class="person">KIERAN BELL</p>
      <p class="role">Managing Director</p>
      <ul>
        <li>
          <svg viewBox="0 0 16 16"><rect width="16" height="16" rx="2" fill="var(--green)"/><path d="M5 3.5l1.8 2.2-1 1.2c.7 1.4 1.8 2.5 3.2 3.2l1.2-1 2.2 1.8-.9 1.6C8 12.3 3.8 8 3.5 4.4z" fill="#fff"/></svg>
          0418 539 746
        </li>
        <li>
          <svg viewBox="0 0 16 16"><rect width="16" height="16" rx="2" fill="var(--green)"/><path d="M5 3.5l1.8 2.2-1 1.2c.7 1.4 1.8 2.5 3.2 3.2l1.2-1 2.2 1.8-.9 1.6C8 12.3 3.8 8 3.5 4.4z" fill="#fff"/></svg>
          (02) 6193 4827
        </li>
        <li>
          <svg viewBox="0 0 16 16"><rect width="16" height="16" rx="2" fill="var(--green)"/><rect x="3" y="4.5" width="10" height="7" fill="none" stroke="#fff" stroke-width="1.2"/><path d="M3 4.5l5 4 5-4" fill="none" stroke="#fff" stroke-width="1.2"/></svg>
          info@harlowiw.com.au
        </li>
        <li>
          <svg viewBox="0 0 16 16"><rect width="16" height="16" rx="2" fill="var(--green)"/><circle cx="8" cy="8" r="4.8" fill="none" stroke="#fff" stroke-width="1.1"/><path d="M3.2 8h9.6M8 3.2c-2 2.6-2 7 0 9.6M8 3.2c2 2.6 2 7 0 9.6" fill="none" stroke="#fff" stroke-width="1"/></svg>
          www.harlowiw.com.au
        </li>
      </ul>
    </div>

    <svg class="foot-bands" viewBox="0 0 680 60" aria-hidden="true">
      <polygon points="0,48 290,48 290,60 0,60" fill="var(--steel-light)"/>
      <polygon points="270,60 300,34 680,34 680,60" fill="var(--green)"/>
    </svg>
  </section>

</body>
</html>
```